Modern Design Business Card industrial maintenance company

Business card design for Company named Brookvale Equipment Services

Target Market(s)

Industrial

Industry/Entity Type

Maintenance and repair

Contact Information for Business Card

Place holder for address, office phone, mobile number and email

Requirements
Must have
• Clean modern look
Nice to have
• N/a

```html
<!DOCTYPE html>
<html lang="en">
<head>
<meta charset="utf-8">
<title>Brookvale Equipment Services – Business Card</title>
<link rel="stylesheet" href="https://fonts.googleapis.com/css2?family=Montserrat:wght@300;600;700&family=Lato:wght@400&display=swap">
<style>
  :root {
    --backdrop: #3b3b3b;
    --card-white: #ffffff;
    --card-black: #151515;
    --card-black-soft: #232323;
    --ink: #111111;
    --ink-muted: #555555;
    --rule: #9a9a9a;
    --on-dark: #f2f2f2;
  }
  * { box-sizing: border-box; margin: 0; padding: 0; }
  html, body {
    width: 1200px; height: 803px; overflow: hidden;
    background: var(--backdrop);
  }
  .stage {
    width: 1200px; height: 803px;
    display: flex; align-items: center; justify-content: center; gap: 40px;
  }
  .card {
    width: 520px; height: 297px; border-radius: 22px;
    position: relative; overflow: hidden;
    box-shadow: 0 14px 30px rgba(0,0,0,.35);
  }

  /* Front */
  .card--front { background: var(--card-white); color: var(--ink); }
  .brand {
    position: absolute; left: 24px; top: 66px; width: 230px;
    display: flex; flex-direction: column; align-items: center; gap: 12px;
    text-align: center;
  }
  .brand__mark {
    width: 58px; height: 58px; flex: none;
    border: 3px solid var(--ink); border-radius: 50%;
  }
  .brand__name {
    font-family: "Montserrat", sans-serif; font-weight: 600;
    font-size: 14px; line-height: 1.3; letter-spacing: .08em;
    text-transform: uppercase; color: var(--ink);
  }
  .divider {
    position: absolute; left: 268px; top: 34px; width: 1px; height: 190px;
    background: linear-gradient(to bottom, transparent, var(--rule) 20%, var(--rule) 80%, transparent);
  }
  .contact { position: absolute; left: 292px; top: 40px; right: 20px; }
  .contact__name {
    font-family: "Montserrat", sans-serif; font-weight: 700;
    font-size: 19px; letter-spacing: .04em; text-transform: uppercase;
  }
  .contact__role {
    font-family: "Montserrat", sans-serif; font-weight: 300;
    font-size: 11px; letter-spacing: .08em; text-transform: uppercase;
    color: var(--ink-muted); margin: 3px 0 16px;
  }
  .contact__list { list-style: none; }
  .contact__item {
    display: flex; align-items: center; gap: 10px;
    font-family: "Lato", sans-serif; font-size: 12px;
    margin-bottom: 9px; letter-spacing: .02em; white-space: nowrap;
  }
  .contact__item svg { width: 14px; height: 14px; flex: none; fill: var(--ink); }
  .address {
    position: absolute; left: 36px; right: 36px; bottom: 30px;
    font-family: "Lato", sans-serif; font-size: 13px; text-align: center;
  }

  /* Back */
  .card--back {
    background: radial-gradient(ellipse at 70% 30%, var(--card-black-soft), var(--card-black) 70%);
  }
  .card__pattern { position: absolute; inset: 0; }
  .brand--reversed {
    left: auto; right: 36px; top: auto; bottom: 44px; width: auto;
    flex-direction: row; gap: 12px; text-align: left;
  }
  .brand--reversed .brand__mark { width: 46px; height: 46px; border-color: var(--on-dark); }
  .brand--reversed .brand__name { color: var(--on-dark); }
</style>
</head>
<body>
<main class="stage">
  <section class="card card--front" aria-label="Business card front">
    <div class="brand">
      <span class="brand__mark"></span>
      <span class="brand__name">Brookvale<br>Equipment Services</span>
    </div>
    <div class="divider"></div>
    <div class="contact">
      <h1 class="contact__name">Daniel Hart</h1>
      <p class="contact__role">Managing Director</p>
      <ul class="contact__list">
        <li class="contact__item">
          <svg viewBox="0 0 16 16"><rect x="1" y="5" width="14" height="10" rx="2"/><path d="M2 5 Q8 0 14 5 L12 6 Q8 3 4 6Z"/></svg>
          044-210 387 654
        </li>
        <li class="contact__item">
          <svg viewBox="0 0 16 16"><path d="M4 1 L6 5 L4.5 6.5 Q6 10 9.5 11.5 L11 10 L15 12 L13.5 15 Q4 14 1 2.5Z"/></svg>
          01 7350 42 18
        </li>
        <li class="contact__item">
          <svg viewBox="0 0 16 16"><path d="M1 3 H15 V13 H1Z"/><path d="M2 4 L8 9 L14 4" stroke="#fff" stroke-width="1.2" fill="none"/></svg>
          DHART@BROOKVALE-ES.COM
        </li>
        <li class="contact__item">
          <svg viewBox="0 0 16 16"><circle cx="8" cy="8" r="7"/><path d="M1 8 H15 M8 1 Q4 8 8 15 M8 1 Q12 8 8 15" stroke="#fff" stroke-width="1" fill="none"/></svg>
          WWW.BROOKVALE-ES.COM
        </li>
      </ul>
    </div>
    <p class="address">318 Harbour Row, Millbrook 45870, Eastland</p>
  </section>

  <section class="card card--back" aria-label="Business card back">
    <div class="card__pattern" role="img" aria-label="Repeating glossy embossed brand pattern on black"></div>
    <div class="brand brand--reversed">
      <span class="brand__mark"></span>
      <span class="brand__name">Brookvale<br>Equipment Services</span>
    </div>
  </section>
</main>
</body>
</html>
```